PROFESSIONAL MODERN REDESIGN OF CURRENT WEBSITE USING ALL SAME CONTENT

I need to redesign existing website using all existing exact content. Please do not leave anything missing. Use all content.

www.brightpathpromotionsgroup.biz

Target Market(s)

Small business owners, business to business, B2B

Industry/Entity Type

Direct Marketing

Number of Pages Required

5+ page

Colors

Designer to choose colors to be used in the design.

Requirements
Must have
• Must use exact same content as www.brightpathpromotionsgroup.biz
Nice to have
• I'd like this to be an easy to read professionally designed website with all modern elements...
Should not have
• Open

```html
<!DOCTYPE html>
<html lang="en">
<head>
<meta charset="utf-8">
<title>Brightpath Promotions Group</title>
<link href="https://fonts.googleapis.com/css2?family=Montserrat:wght@300;400;600;700&family=Open+Sans:wght@400;600;700&display=swap" rel="stylesheet">
<style>
:root{
  --blue:#1f7ac7;
  --blue-dark:#145b9b;
  --orange:#f7a81b;
  --ink:#3a3f45;
  --muted:#7a828b;
  --line:#e2e6ea;
  --paper:#ffffff;
  --soft:#f3f5f7;
  --footer:#1e2225;
  --footer-bar:#15181a;
}
*{box-sizing:border-box;margin:0;padding:0}
html,body{width:1200px;height:5224px;overflow:hidden}
body{font-family:"Open Sans",sans-serif;color:var(--ink);background:var(--paper);font-size:13px;line-height:1.6}
.section{position:relative;width:1200px;overflow:hidden}
h1,h2,h3{font-family:"Montserrat",sans-serif}
.btn{display:inline-block;font-family:"Montserrat",sans-serif;font-weight:700;font-size:11px;letter-spacing:.6px;text-transform:uppercase;padding:10px 26px;border-radius:22px;color:#fff;text-decoration:none;white-space:nowrap}
.btn-orange{background:var(--orange)}
.btn-blue{background:var(--blue)}
.btn-row{position:absolute;left:0;width:1200px;text-align:center}
.photo{border-radius:4px}

/* header */
.topbar{height:88px;background:var(--paper)}
.brand{position:absolute;left:120px;top:24px;display:flex;align-items:center;gap:10px}
.brand-mark{width:40px;height:40px;background:var(--blue);border-radius:4px}
.brand-name{font-family:"Montserrat",sans-serif;font-weight:700;font-size:20px;color:var(--blue);letter-spacing:.5px;text-transform:uppercase}
.topbar .btn{position:absolute;right:120px;top:30px;padding:7px 16px;font-size:10px}
.nav{height:40px;background:var(--blue)}
.nav ul{position:absolute;left:120px;top:0;display:flex;list-style:none}
.nav li{font-family:"Montserrat",sans-serif;font-size:11px;font-weight:600;color:#fff;padding:0 22px;line-height:40px;text-transform:uppercase}
.nav li.active{background:#fff;color:var(--blue)}

/* hero */
.hero{height:512px;background:linear-gradient(180deg,#f7f9fb,#eef2f5)}
.hero h1{position:absolute;left:120px;top:210px;width:460px;font-weight:400;font-size:32px;line-height:1.25;color:var(--blue)}
.hero .btn{position:absolute;left:120px;top:372px}
.hero .photo{position:absolute;left:600px;top:24px;width:480px;height:440px;background:linear-gradient(135deg,#cfd8e0,#8fa7bb)}

/* incentives */
.incentives{height:660px}
.lead{position:absolute;left:150px;top:60px;width:900px;text-align:center;font-weight:300;font-size:26px;line-height:1.3;color:var(--blue);text-transform:uppercase}
.cards{position:absolute;left:120px;top:190px;width:960px;display:flex;gap:20px}
.card{width:225px;height:280px;border:1px solid var(--line);border-radius:4px;padding:16px;box-shadow:0 2px 6px rgba(0,0,0,.06)}
.card h3{font-size:13px;font-weight:600;color:var(--ink);margin-bottom:10px;height:36px;line-height:1.35}
.card .photo{height:96px;margin-bottom:12px}
.card p{font-size:10px;color:var(--muted);line-height:1.5;height:64px}
.card .price{color:var(--blue);font-weight:600}
.card .more{font-family:"Montserrat",sans-serif;font-size:9px;font-weight:700;color:var(--blue);text-transform:uppercase}
.incentives .btn-row{top:596px}

/* orange areas */
.areas{height:950px;background:var(--orange)}
.areas .wave{position:absolute;left:0;width:1200px}
.areas h2{position:absolute;left:200px;top:180px;width:800px;text-align:center;color:#fff;font-weight:300;font-size:28px;line-height:1.3;text-transform:uppercase}
.grid{position:absolute;left:240px;top:320px;width:720px;display:grid;grid-template-columns:1fr 1fr;gap:36px 60px}
.area{display:flex;gap:16px}
.icon{flex:none;width:50px;height:50px;border-radius:50%;background:var(--blue);display:flex;align-items:center;justify-content:center}
.area h3{font-size:15px;font-weight:600;color:#fff;margin-bottom:4px}
.area p{font-size:11px;color:#fff;line-height:1.5}
.areas .btn-row{top:740px}

/* distribution */
.distribution{height:610px}
.tabs{position:absolute;left:300px;top:30px;display:flex;width:600px;border-bottom:2px solid var(--blue)}
.tab{width:300px;line-height:40px;text-align:center;font-family:"Montserrat",sans-serif;font-size:11px;font-weight:700;text-transform:uppercase;color:var(--muted);background:var(--soft)}
.tab.active{background:var(--blue);color:#fff}
.distribution h2{position:absolute;left:0;width:1200px;top:140px;text-align:center;font-weight:300;font-size:30px;color:var(--blue);text-transform:uppercase}
.channels{position:absolute;left:150px;top:240px;width:900px;display:flex;gap:30px}
.channel{width:202px}
.channel .icon{width:36px;height:36px;background:none;border-radius:0;justify-content:flex-start;margin-bottom:6px}
.channel h3{font-size:14px;font-weight:600;color:var(--ink);margin-bottom:6px}
.channel p{font-size:10px;color:var(--muted);line-height:1.55}
.distribution .btn-row{top:530px}

/* protect */
.protect{height:580px;background:var(--blue)}
.protect .wave{position:absolute;left:0;width:1200px}
.protect .photo{position:absolute;left:120px;top:140px;width:440px;height:280px;background:linear-gradient(135deg,#b8c6d3,#5f7a92)}
.protect h2{position:absolute;left:610px;top:140px;width:470px;color:#fff;font-weight:300;font-size:26px;line-height:1.25;text-transform:uppercase}
.protect .copy{position:absolute;left:610px;top:220px;width:470px;color:#fff;font-size:10px;line-height:1.6}
.protect .copy p{margin-bottom:10px}
.protect .btn{position:absolute;left:610px;top:420px}

/* how */
.how{height:520px}
.side{position:absolute;left:120px;top:40px;width:230px;list-style:none;border:1px solid var(--line)}
.side li{font-family:"Montserrat",sans-serif;font-size:11px;font-weight:700;text-transform:uppercase;color:var(--muted);padding:0 20px;line-height:56px;border-bottom:1px solid var(--line)}
.side li.active{background:var(--blue);color:#fff}
.how h2{position:absolute;left:390px;top:40px;font-weight:300;font-size:22px;color:var(--blue);text-transform:uppercase}
.how .copy{position:absolute;left:390px;top:82px;width:690px;font-size:11px;line-height:1.7;color:var(--ink)}
.how .copy p{margin-bottom:12px}
.how .btn{position:absolute;left:390px;top:440px}

/* partners */
.partners{height:540px;background:var(--soft)}
.logos{position:absolute;left:130px;top:50px;width:940px;display:flex;justify-content:space-between;align-items:center}
.logo-name{font-family:"Open Sans",sans-serif;font-size:26px;font-weight:600;color:#5b6067}
.quote{position:absolute;left:120px;top:140px;width:960px;height:200px;background:#fff;border:4px solid var(--orange);border-radius:6px;padding:40px 130px;text-align:center}
.quote p{font-family:"Montserrat",sans-serif;font-size:16px;font-weight:600;color:var(--blue);line-height:1.45}
.quote .who{margin-top:12px;font-size:10px;color:var(--muted);font-family:"Open Sans",sans-serif;font-weight:600}
.quote .mark{position:absolute;top:24px;font-family:"Montserrat",sans-serif;font-size:60px;color:var(--orange);line-height:1}
.partners .btn-row{top:430px}

/* affiliate */
.affiliate{height:340px;background:linear-gradient(90deg,#f4f8fc 0%,#f4f8fc 38%,var(--blue) 38%,var(--blue-dark) 100%)}
.affiliate .photo{position:absolute;left:70px;top:50px;width:360px;height:240px;background:linear-gradient(135deg,#dfe6ec,#a9bccd)}
.affiliate h2{position:absolute;left:500px;top:90px;width:560px;color:#fff;font-weight:400;font-size:22px;line-height:1.3}
.affiliate h2 strong{font-weight:600}
.affiliate .link{position:absolute;left:500px;top:250px;color:#fff;font-family:"Montserrat",sans-serif;font-weight:700;font-size:11px;text-transform:uppercase}

/* footer */
.footer{height:384px;background:var(--footer);color:#c8cdd2}
.footer h4{font-family:"Montserrat",sans-serif;font-size:11px;color:#fff;text-transform:uppercase;letter-spacing:.5px;margin-bottom:14px}
.fcol{position:absolute;top:40px}
.fcol ul{list-style:none}
.fcol li{font-size:11px;line-height:22px}
.fcol li::before{content:"› ";color:var(--orange)}
.contact p{font-size:11px;line-height:1.7;padding-left:20px;position:relative;margin-bottom:8px}
.contact svg{position:absolute;left:0;top:3px}
.social{display:flex;gap:8px;margin-top:14px}
.social span{width:24px;height:24px;border-radius:3px;background:#c83a2e}
.legal{position:absolute;left:0;bottom:0;width:1200px;height:44px;background:var(--footer-bar);font-size:10px;color:#8a9096;line-height:44px;padding-left:120px}
.chat{position:absolute;right:24px;bottom:54px;width:40px;height:40px;border-radius:50%;background:#e0453a}
</style>
</head>
<body>

<header class="section topbar">
  <div class="brand"><span class="brand-mark"></span><span class="brand-name">Brightpath Promotions Group</span></div>
  <a class="btn btn-orange" href="#">Get Started</a>
</header>
<nav class="section nav">
  <ul>
    <li class="active">Home</li><li>Our Incentives</li><li>Samples</li><li>Affiliates</li><li>Testimonials</li><li>FAQ</li><li>Contact</li>
  </ul>
</nav>

<section class="section hero">
  <h1>Boost Sales From Your Existing Marketing Efforts Creating Exciting Promotions.</h1>
  <a class="btn btn-orange" href="#">Quick 30 Day Risk Free Trial</a>
  <div class="photo" role="img" aria-label="Desktop computer showing a vacation promotion with happy travellers"></div>
</section>

<section class="section incentives">
  <h2 class="lead">For $99/mth you can attract more customers by creating exciting promotional giveaways using an unlimited amount of gift certificates redeemable for:</h2>
  <div class="cards">
    <div class="card">
      <h3>Vacation Getaway Certificates</h3>
      <div class="photo" role="img" aria-label="Resort pool and beach getaway scene" style="background:linear-gradient(135deg,#9ed0e6,#3f8fb8)"></div>
      <p>Resort stays, cruises &amp; airfares. Up to <span class="price">$5000.00</span> retail value. Your customers just pay taxes.</p>
      <span class="more">View the certificates →</span>
    </div>
    <div class="card">
      <h3>Restaurant Gift Certificates</h3>
      <div class="photo" role="img" aria-label="Plated restaurant dinner" style="background:linear-gradient(135deg,#e6c79e,#a86b3c)"></div>
      <p><span class="price">$25-$100</span> retail value. Thousands of restaurants nationwide.</p>
      <span class="more">View the dashboard →</span>
    </div>
    <div class="card">
      <h3>Electronic Product Giveaways</h3>
      <div class="photo" role="img" aria-label="Tablets, headphones and gadgets" style="background:linear-gradient(135deg,#c9ced4,#6b7580)"></div>
      <p>HD tablets, premium earbuds, smart watches, more players. <span class="price">$50-$500</span> retail value.</p>
      <span class="more">View the incentives →</span>
    </div>
    <div class="card">
      <h3>Gas, Grocery &amp; Wine Vouchers</h3>
      <div class="photo" role="img" aria-label="Grocery bag, fuel pump and wine bottles" style="background:linear-gradient(135deg,#d6e3b8,#7d9a4a)"></div>
      <p><span class="price">$25-$500</span> denominations. Redeemed at national stores.</p>
      <span class="more">View the vouchers →</span>
    </div>
  </div>
  <div class="btn-row"><a class="btn btn-blue" href="#">Get a 100% Free Sample Package</a></div>
</section>

<section class="section areas">
  <svg class="wave" style="top:0" width="1200" height="110" viewBox="0 0 1200 110" aria-hidden="true"><path d="M0 0H1200V40C900 110 400 110 0 30Z" fill="#fff"/></svg>
  <h2>We plug right into your<br>existing advertising in 4 major areas</h2>
  <div class="grid">
    <div class="area">
      <span class="icon"><svg width="24" height="24" viewBox="0 0 24 24"><path d="M3 10v4h4l6 4V6L7 10H3zm14-1v6" stroke="#fff" stroke-width="2" fill="none"/></svg></span>
      <div><h3>Boost Response Rates To Your Existing Ads</h3><p>Add a simple headline to all your ads. Offer a free getaway and watch more readers call, click and visit you today.</p></div>
    </div>
    <div class="area">
      <span class="icon"><svg width="24" height="24" viewBox="0 0 24 24"><path d="M4 12a8 8 0 0 1 14-5M20 12a8 8 0 0 1-14 5M18 3v4h-4M6 21v-4h4" stroke="#fff" stroke-width="2" fill="none"/></svg></span>
      <div><h3>Increase Repeat &amp; Referral Business</h3><p>Reward loyal buyers with a bonus gift so they return again, and give extra certificates for every friend they send over.</p></div>
    </div>
    <div class="area">
      <span class="icon"><svg width="24" height="24" viewBox="0 0 24 24"><circle cx="10" cy="8" r="4" stroke="#fff" stroke-width="2" fill="none"/><path d="M3 20c0-4 3-6 7-6s7 2 7 6M19 8v6M16 11h6" stroke="#fff" stroke-width="2" fill="none"/></svg></span>
      <div><h3>Gain More New Customers</h3><p>New prospects act faster when a valuable gift is attached to their first purchase, so your ads convert far better.</p></div>
    </div>
    <div class="area">
      <span class="icon"><svg width="24" height="24" viewBox="0 0 24 24"><path d="M4 18l5-6 4 3 7-9" stroke="#fff" stroke-width="2" fill="none"/></svg></span>
      <div><h3>Boost Your Referral Business</h3><p>Hand out a free certificate to each new referral and let happy customers spread the word about you for you.</p></div>
    </div>
  </div>
  <div class="btn-row"><a class="btn btn-blue" href="#">Quick 30 Day Risk Free Sign Up</a></div>
  <svg class="wave" style="bottom:0" width="1200" height="110" viewBox="0 0 1200 110" aria-hidden="true"><path d="M0 110H1200V40C800 120 300 0 0 70Z" fill="#fff"/></svg>
</section>

<section class="section distribution">
  <div class="tabs"><div class="tab active">Easy Distribution</div><div class="tab">Marketing Materials</div></div>
  <h2>Easy Distribution of Incentives</h2>
  <div class="channels">
    <div class="channel">
      <span class="icon"><svg width="30" height="30" viewBox="0 0 24 24"><path d="M6 9V3h12v6M6 18H3v-8h18v8h-3M6 14h12v7H6z" stroke="#f7a81b" stroke-width="2" fill="none"/></svg></span>
      <h3>Print</h3><p>Download PDF certificates to print and physically hand them out or mail them to your customers.</p>
    </div>
    <div class="channel">
      <span class="icon"><svg width="30" height="30" viewBox="0 0 24 24"><rect x="3" y="5" width="18" height="14" stroke="#f7a81b" stroke-width="2" fill="none"/><path d="M3 6l9 7 9-7" stroke="#f7a81b" stroke-width="2" fill="none"/></svg></span>
      <h3>E-Mail</h3><p>Email e-certificates to your customers individually or in bulk with just one click.</p>
    </div>
    <div class="channel">
      <span class="icon"><svg width="30" height="30" viewBox="0 0 24 24"><rect x="3" y="4" width="18" height="13" stroke="#f7a81b" stroke-width="2" fill="none"/><path d="M8 21h8M12 17v4" stroke="#f7a81b" stroke-width="2"/></svg></span>
      <h3>Web Banners or API Integration</h3><p>Install our HTML web banners on the thank-you pages of your website to automate distribution of certificates, or link our API to your system.</p>
    </div>
    <div class="channel">
      <span class="icon"><svg width="30" height="30" viewBox="0 0 24 24"><rect x="6" y="2" width="12" height="20" rx="2" stroke="#f7a81b" stroke-width="2" fill="none"/><path d="M11 18h2" stroke="#f7a81b" stroke-width="2"/></svg></span>
      <h3>SMS/Text Messaging</h3><p>Send certificates through text messaging with just one click with our SMS feature at no extra cost.</p>
    </div>
  </div>
  <div class="btn-row"><a class="btn btn-blue" href="#">Click Here We Will Call You</a></div>
</section>

<section class="section protect">
  <svg class="wave" style="top:0" width="1200" height="80" viewBox="0 0 1200 80" aria-hidden="true"><path d="M0 0H1200V20C800 90 400 80 0 40Z" fill="#fff"/></svg>
  <div class="photo" role="img" aria-label="Laptop playing an introduction video with a presenter"></div>
  <h2>We protect the integrity of your promotions</h2>
  <div class="copy">
    <p>Your and fearsome name, a marketing company, so we want to protect the integrity of your promotions.</p>
    <p>We allow you to brand the certificate with your company info. For every certificate there is a "Compliments Of" area where we allow you to put up to 3 lines of text and a logo.</p>
    <p>On the flip side of that, we don't advertise our name anywhere on the certificates or on our redemption website, because we don't want your customers to find out how much you paid for them. The whole magic of our program is the difference between the perceived value that your customers see and what it's actually costing you.</p>
  </div>
  <a class="btn btn-orange" href="#">Click Here We Will Call You</a>
  <svg class="wave" style="bottom:0" width="1200" height="80" viewBox="0 0 1200 80" aria-hidden="true"><path d="M0 80H1200V30C800 90 300 10 0 60Z" fill="#fff"/></svg>
</section>

<section class="section how">
  <ul class="side">
    <li class="active">How do we do it?</li><li>Customer Service</li><li>Who we are</li><li>Our History</li>
  </ul>
  <h2>How do we do it?</h2>
  <div class="copy">
    <p>It's very important for you to understand how we are able to do this. First off, hotels and resorts are rarely full, and they are always open and still have their fixed costs. They have vacant rooms available, so what they do is hook up with marketing companies like us to help them fill up their otherwise empty rooms. That way they end up turning into additional revenue from other parts of their property like their in-house restaurants, the bar, the casino, resort activities, the spa as well as extra day trips.</p>
    <p>They're actually doing it for some of the same reasons why you would be using our certificates: to increase their repeat and referral business. They know that if they show your customers a good time while they're there, they'll be more likely to tell their friends and family about the great time they had and will be more likely to book with the property in the future as a regular paying customer.</p>
    <p>The same idea holds for our restaurant, electronics, gas, grocery and wine partners. They gain new paying guests and buyers, while you gain a powerful incentive for a small flat monthly fee.</p>
  </div>
  <a class="btn btn-blue" href="#">Get a 100% Free Sample Package</a>
</section>

<section class="section partners">
  <div class="logos">
    <span class="logo-name">Quillmarsh</span>
    <span class="logo-name">Brennova</span>
    <span class="logo-name">Halvorend</span>
    <span class="logo-name">Tessaly Glass</span>
  </div>
  <div class="quote">
    <span class="mark" style="left:40px">“</span>
    <p>I have experienced a 40% increase in lead captures. I recommend BPG to anyone looking for an effective marketing tool to help expand their business and increase their income.</p>
    <div class="who">— Kim C.</div>
    <span class="mark" style="right:40px">”</span>
  </div>
  <div class="btn-row"><a class="btn btn-orange" href="#">Quick 30 Day Risk Free Trial Sign Up</a></div>
</section>

<section class="section affiliate">
  <div class="photo" role="img" aria-label="Laptop displaying the affiliate program page"></div>
  <h2>Know Any Businesses That Could Benefit Using Incentives To Bring In More Customers?<br><strong>Earn 40% RESIDUAL COMMISSIONS as an AFFILIATE!</strong></h2>
  <span class="link">Learn More →</span>
</section>

<footer class="section footer">
  <div class="fcol" style="left:120px"><h4>Links</h4><ul><li>Home</li><li>Our Incentives</li><li>Samples</li><li>Affiliates</li><li>Testimonials</li><li>FAQ</li></ul></div>
  <div class="fcol" style="left:320px"><h4>&nbsp;</h4><ul><li>Contact Us</li><li>Terms &amp; Conditions</li><li>Privacy Policy</li><li>Helpline</li><li>BPG PDF Flyer</li></ul></div>
  <div class="fcol" style="left:540px"><h4>&nbsp;</h4><ul><li>BPG PDF Brochure</li><li>BPG Certificate List</li><li>How To Use BPG Certificates</li><li>Free Video Ad Mock Up For Marketing</li></ul></div>
  <div class="fcol contact" style="left:840px;width:240px"><h4>Contact Us</h4>
    <p><svg width="12" height="12" viewBox="0 0 24 24"><path d="M12 2a7 7 0 0 0-7 7c0 5 7 13 7 13s7-8 7-13a7 7 0 0 0-7-7z" fill="#f7a81b"/></svg>Brightpath Promotions Group, Inc.<br>4120 Meadowrun Ave, Suite 210<br>Fairview, CA 90000</p>
    <p><svg width="12" height="12" viewBox="0 0 24 24"><circle cx="12" cy="12" r="9" stroke="#f7a81b" stroke-width="3" fill="none"/></svg>Hours: Mon–Fri 9am – 5pm PST</p>
    <p><svg width="12" height="12" viewBox="0 0 24 24"><path d="M5 3h4l2 5-3 2a11 11 0 0 0 6 6l2-3 5 2v4a2 2 0 0 1-2 2A17 17 0 0 1 3 5a2 2 0 0 1 2-2z" fill="#f7a81b"/></svg>(555) 014-2290</p>
    <div class="social"><span></span><span></span><span></span><span></span><span></span></div>
  </div>
  <span class="chat"></span>
  <div class="legal">Copyright 2005-2020 Brightpath Promotions Group, Inc. All rights reserved.</div>
</footer>

</body>
</html>
```